Visitenkarten-Design für Boutique-Unternehmensberatung
Zielgruppe
Boutique Unternehmensberatung für die Chemische Industrie. Wir unterstützen Unternehmen, die Beziehung zu Ihren Händlern zu optimieren.
Vorläufige Website handelsbruecke-nord.de kann ggf weitere Einblicke geben. Hinweis: Diese Website wurde bisher noch nicht professionell erstellt.
Aufgabenstellung
Die Visitenkarte sollte vertrauenserweckend und seriös wirken. Zeitgleich aber auch modern.

```html
<!DOCTYPE html>
<html lang="de">
<head>
<meta charset="utf-8">
<title>Visitenkarte – Handelsbrücke Nord</title>
<link rel="stylesheet" href="https://fonts.googleapis.com/css2?family=Poppins:wght@300;400;600;700&display=swap">
<style>
  :root {
    --brand-blue: #1d4a82;
    --card-white: #ffffff;
    --backdrop: #eceef1;
    --text-blue: #1d4a82;
    --shadow: rgba(20, 30, 50, 0.18);
  }
  * { box-sizing: border-box; margin: 0; padding: 0; }
  html, body {
    width: 1200px; height: 720px; overflow: hidden;
    background: var(--backdrop);
    font-family: "Poppins", sans-serif;
  }
  .stage {
    position: relative; width: 1200px; height: 720px;
    display: flex; align-items: center; justify-content: center; gap: 60px;
  }
  .card {
    width: 520px; height: 336px; position: relative;
    border-radius: 4px;
    box-shadow: 0 14px 30px var(--shadow);
  }
  .card--front { background: var(--card-white); color: var(--text-blue); }
  .card--back { background: var(--brand-blue); color: var(--card-white); }

  .brand {
    display: flex; align-items: center; gap: 12px;
    font-weight: 600; line-height: 1.05;
  }
  .brand__dot { border-radius: 50%; flex: none; }
  .card--front .brand {
    position: absolute; left: 60px; top: 48px; font-size: 24px;
  }
  .card--front .brand__dot { width: 44px; height: 44px; background: var(--brand-blue); }

  .contact {
    position: absolute; left: 290px; top: 118px;
    font-size: 12.5px; font-weight: 300; line-height: 1.35;
    list-style: none;
  }
  .contact__item { display: flex; gap: 12px; align-items: flex-start; margin-bottom: 10px; }
  .contact__icon { width: 16px; height: 16px; flex: none; margin-top: 1px; }

  .person { position: absolute; left: 36px; bottom: 70px; }
  .person__name {
    font-size: 24px; font-weight: 700; letter-spacing: 0.5px; text-transform: uppercase;
  }
  .person__role {
    font-size: 13px; font-weight: 400; letter-spacing: 0.6px; text-transform: uppercase;
  }

  .card--back .brand {
    position: absolute; left: 50%; top: 120px; transform: translateX(-50%);
    flex-direction: column; text-align: center; font-size: 30px; gap: 16px;
  }
  .card--back .brand__dot { width: 60px; height: 60px; background: var(--card-white); }
  .web {
    position: absolute; left: 0; right: 0; bottom: 26px; text-align: center;
    font-size: 13px; font-weight: 300; letter-spacing: 0.3px;
  }
</style>
</head>
<body>
<main class="stage">
  <section class="card card--front" aria-label="Vorderseite der Visitenkarte">
    <div class="brand">
      <span class="brand__dot"></span>
      <span class="brand__name">Handelsbrücke<br>Nord</span>
    </div>

    <ul class="contact">
      <li class="contact__item">
        <svg class="contact__icon" viewBox="0 0 16 16" fill="none" stroke="currentColor" stroke-width="1.3" aria-hidden="true">
          <path d="M8 15s5-5 5-8.5A5 5 0 0 0 3 6.5C3 10 8 15 8 15z"/>
          <circle cx="8" cy="6.5" r="1.8"/>
        </svg>
        <span>Handelsbrücke Nord GmbH<br>Lindenkai 7<br>28195 Bremen</span>
      </li>
      <li class="contact__item">
        <svg class="contact__icon" viewBox="0 0 16 16" fill="none" stroke="currentColor" stroke-width="1.3" aria-hidden="true">
          <path d="M4 1.5h2l1 3.5-1.5 1a8 8 0 0 0 4.5 4.5l1-1.5 3.5 1v2a2 2 0 0 1-2 2A11 11 0 0 1 2 3.5a2 2 0 0 1 2-2z"/>
        </svg>
        <span>+49 421 / 555 020 40</span>
      </li>
      <li class="contact__item">
        <svg class="contact__icon" viewBox="0 0 16 16" fill="none" stroke="currentColor" stroke-width="1.3" aria-hidden="true">
          <rect x="1.5" y="3.5" width="13" height="9" rx="1"/>
          <path d="M1.5 4l6.5 5 6.5-5"/>
        </svg>
        <span>mail@handelsbruecke-nord.de</span>
      </li>
    </ul>

    <div class="person">
      <p class="person__name">Henrik Valdorf</p>
      <p class="person__role">Geschäftsführer</p>
    </div>
  </section>

  <section class="card card--back" aria-label="Rückseite der Visitenkarte">
    <div class="brand">
      <span class="brand__dot"></span>
      <span class="brand__name">Handelsbrücke<br>Nord</span>
    </div>
    <p class="web">www.handelsbruecke-nord.de</p>
  </section>
</main>
</body>
</html>
```